Australian IT Company requires Business Card Design

Bluewattle is an Australian company that specialises in IT consulting & support, software development, project management, network services.

We have been in business for 15 years.

* We require a business card with the following on it:
Logo
Address
Contact Details
Space for staff name, title & mobile number

Industry/Entity Type

Software

```html
<!DOCTYPE html>
<html lang="en">
<head>
<meta charset="utf-8">
<title>Bluewattle business card options</title>
<link rel="stylesheet" href="https://fonts.googleapis.com/css2?family=Open+Sans:wght@400;600;700&display=swap">
<style>
  :root {
    --page-bg: #ebeced;
    --brand-blue: #3d6a96;
    --band-dark: #223a58;
    --band-mid: #2c4b70;
    --band-light: #3e6891;
    --silver-light: #ffffff;
    --silver-dark: #b9bbbf;
    --tagline-grey: #5f6166;
    --address-accent: #8fbbe8;
    --label-ink: #333333;
    --white: #ffffff;
  }
  html, body {
    margin: 0;
    padding: 0;
    width: 1017px;
    height: 1200px;
    overflow: hidden;
    background: var(--page-bg);
    font-family: "Open Sans", Arial, sans-serif;
  }
  .option-label {
    position: absolute;
    left: 34px;
    font-size: 40px;
    color: var(--label-ink);
    font-weight: 400;
  }
  .option-label--one { top: 266px; }
  .option-label--two { top: 896px; }
  .business-card {
    position: absolute;
    left: 103px;
    width: 856px;
    height: 494px;
    filter: drop-shadow(6px 6px 7px rgba(0,0,0,0.28));
  }
  .business-card--silver { top: 75px; }
  .business-card--white { top: 651px; }
  .wordmark { font-weight: 600; fill: var(--brand-blue); font-size: 60px; }
  .tagline { font-size: 16px; fill: var(--tagline-grey); letter-spacing: 3px; }
  .staff-name { font-weight: 700; font-size: 23px; fill: var(--white); }
  .staff-role, .contact-line { font-size: 21px; fill: var(--white); }
  .address-line--accent { font-weight: 700; fill: var(--address-accent); }
  .website { font-weight: 700; font-size: 25px; fill: var(--brand-blue); }
  .icon-stroke { fill: none; stroke: var(--white); stroke-width: 1.6; }
  .icon-fill { fill: var(--white); }
  .business-card--white .address-icon .icon-fill { fill: var(--address-accent); }
  .business-card--white .address-icon .icon-stroke { stroke: var(--address-accent); }
</style>
</head>
<body>

<div class="option-label option-label--one">1</div>
<svg class="business-card business-card--silver" viewBox="0 0 710 410" aria-label="Business card, silver version">
  <defs>
    <linearGradient id="silverFace" x1="0" x2="1" y1="0" y2="0">
      <stop offset="0" stop-color="var(--silver-dark)"/>
      <stop offset="0.35" stop-color="var(--silver-light)"/>
      <stop offset="0.65" stop-color="var(--silver-light)"/>
      <stop offset="1" stop-color="var(--silver-dark)"/>
    </linearGradient>
    <linearGradient id="bandDeep" x1="0" x2="0" y1="0" y2="1">
      <stop offset="0" stop-color="var(--band-dark)"/>
      <stop offset="0.6" stop-color="var(--band-light)"/>
      <stop offset="1" stop-color="var(--band-light)"/>
    </linearGradient>
    <linearGradient id="silverArc" x1="0" x2="1" y1="0" y2="0">
      <stop offset="0" stop-color="#ffffff"/>
      <stop offset="0.5" stop-color="#9ea1a6"/>
      <stop offset="1" stop-color="#6f7277"/>
    </linearGradient>
  </defs>
  <rect width="710" height="410" fill="url(#silverFace)"/>
  <text class="wordmark" x="355" y="92" text-anchor="middle">BLUEWATTLE</text>
  <text class="tagline" x="355" y="128" text-anchor="middle">IT CONSULTING &amp; SOFTWARE SOLUTIONS</text>
  <path d="M0 172 Q355 128 710 172 L710 178 Q355 142 0 178 Z" fill="url(#silverArc)"/>
  <path d="M0 178 Q355 142 710 178 L710 351 L0 351 Z" fill="url(#bandDeep)"/>
  <text class="staff-name" x="355" y="201" text-anchor="middle">Name Surname</text>
  <text class="staff-role" x="355" y="228" text-anchor="middle">Position</text>
  <g transform="translate(260 253)">
    <path class="icon-fill" d="M3 1 L7 1 L8 6 L6 8 Q8 13 12 15 L14 13 L18 14 L18 17 Q17 19 14 19 Q2 15 1 3 Q1 1 3 1 Z"/>
  </g>
  <text class="contact-line" x="279" y="270">+61 3 9284 6150</text>
  <g transform="translate(190 281)">
    <rect class="icon-stroke" x="0.8" y="0.8" width="18" height="13"/>
    <path class="icon-stroke" d="M1 1 L10 9 L19 1"/>
  </g>
  <text class="contact-line" x="215" y="297">name@bluewattle.net.au</text>
  <g class="address-icon" transform="translate(84 320)">
    <path class="icon-fill" d="M0 7 L10 0 L20 7 Z"/>
    <rect class="icon-stroke" x="2" y="7" width="16" height="10"/>
    <rect class="icon-fill" x="8" y="10" width="4" height="7"/>
  </g>
  <text class="contact-line address-line" x="114" y="337">14 Kestrel Road, Suite 3, Hawthorn Vic 3122</text>
  <text class="website" x="355" y="392" text-anchor="middle">www.bluewattle.net.au</text>
</svg>

<div class="option-label option-label--two">2</div>
<svg class="business-card business-card--white" viewBox="0 0 710 410" aria-label="Business card, white version">
  <defs>
    <linearGradient id="bandRise" x1="0" x2="0" y1="0" y2="1">
      <stop offset="0" stop-color="var(--band-light)"/>
      <stop offset="0.55" stop-color="var(--band-mid)"/>
      <stop offset="1" stop-color="var(--band-dark)"/>
    </linearGradient>
    <linearGradient id="silverArcTwo" x1="0" x2="1" y1="0" y2="0">
      <stop offset="0" stop-color="#ffffff"/>
      <stop offset="0.5" stop-color="#a3a6ab"/>
      <stop offset="1" stop-color="#6f7277"/>
    </linearGradient>
  </defs>
  <rect width="710" height="410" fill="var(--white)"/>
  <text class="wordmark" x="355" y="92" text-anchor="middle">BLUEWATTLE</text>
  <text class="tagline" x="355" y="128" text-anchor="middle">IT CONSULTING &amp; SOFTWARE SOLUTIONS</text>
  <path d="M0 172 Q355 128 710 172 L710 178 Q355 142 0 178 Z" fill="url(#silverArcTwo)"/>
  <path d="M0 178 Q355 142 710 178 L710 351 L0 351 Z" fill="url(#bandRise)"/>
  <text class="staff-name" x="355" y="201" text-anchor="middle">Name Surname</text>
  <text class="staff-role" x="355" y="228" text-anchor="middle">Position</text>
  <g transform="translate(260 253)">
    <path class="icon-fill" d="M3 1 L7 1 L8 6 L6 8 Q8 13 12 15 L14 13 L18 14 L18 17 Q17 19 14 19 Q2 15 1 3 Q1 1 3 1 Z"/>
  </g>
  <text class="contact-line" x="279" y="270">+61 3 9284 6150</text>
  <g transform="translate(190 281)">
    <rect class="icon-stroke" x="0.8" y="0.8" width="18" height="13"/>
    <path class="icon-stroke" d="M1 1 L10 9 L19 1"/>
  </g>
  <text class="contact-line" x="215" y="297">name@bluewattle.net.au</text>
  <g class="address-icon" transform="translate(84 320)">
    <path class="icon-fill" d="M0 7 L10 0 L20 7 Z"/>
    <rect class="icon-stroke" x="2" y="7" width="16" height="10"/>
    <rect class="icon-fill" x="8" y="10" width="4" height="7"/>
  </g>
  <text class="contact-line address-line address-line--accent" x="112" y="337">14 Kestrel Road, Suite 3, Hawthorn Vic 3122</text>
  <text class="website" x="355" y="392" text-anchor="middle">www.bluewattle.net.au</text>
</svg>

</body>
</html>
```